Harbor Logistics Business card and letterhead
Professional business card
Professional
Calvin Marsh
Director of Operations
4538 E 61st Pl
Maple Grove, KS 66417-3814
cmarsh@harborlogisticsco.example
http://www.harborlogisticsco.example
Looking for something clean, professional, and simple. Fonts are optional, just flow with fonts in logo
On the back we would like the mission of "Moving Every Day Forward" printed in some design. We would like the background to be a solid design from a logo color with white writing
This is our corporate logo

```html
<!DOCTYPE html>
<html lang="en">
<head>
<meta charset="utf-8">
<title>Harbor Logistics Stationery</title>
<link rel="stylesheet" href="https://fonts.googleapis.com/css2?family=Montserrat:wght@700;800&family=Open+Sans:wght@400;600&display=swap">
<style>
  :root {
    --navy: #0a1230;
    --deep-blue: #0b2f8a;
    --bright-blue: #1e7be8;
    --glow-blue: #49b6ff;
    --green: #2f8f3a;
    --dark-green: #0b2a14;
    --ink: #1a1f2b;
    --muted: #555b66;
    --paper: #ffffff;
    --stage: #ffffff;
  }
  * { box-sizing: border-box; margin: 0; padding: 0; }
  html, body { width: 1200px; height: 737px; overflow: hidden; background: var(--stage); }
  body { position: relative; font-family: "Open Sans", Arial, sans-serif; color: var(--ink); }

  .sheet { position: absolute; background: var(--paper); box-shadow: 0 0 0 1px #e2e4e8, 0 2px 6px rgba(0,0,0,.12); overflow: hidden; }
  .arc-band { position: absolute; left: 0; top: 0; width: 100%; display: block; }

  .brand { position: absolute; left: 0; right: 0; display: flex; flex-direction: column; align-items: center; gap: 6px; }
  .brand-dot { display: block; border-radius: 50%; background: radial-gradient(circle at 35% 35%, var(--glow-blue), var(--deep-blue) 70%); }
  .brand-name { font-family: "Montserrat", Arial, sans-serif; font-weight: 800; color: var(--ink); letter-spacing: .04em; text-transform: uppercase; white-space: nowrap; line-height: 1; }
  .brand-name.on-dark { color: #fff; }

  /* Letterhead */
  .letterhead { left: 17px; top: 7px; width: 552px; height: 696px; }
  .letterhead .brand { top: 34px; gap: 8px; }
  .letterhead .brand-dot { width: 60px; height: 60px; box-shadow: 0 0 0 3px #fff; }
  .letterhead .brand-name { font-size: 18px; }
  .letterhead-footer { position: absolute; bottom: 14px; left: 0; right: 0; text-align: center; font-size: 8.5px; color: var(--muted); }

  /* Envelope */
  .envelope { left: 590px; top: 7px; width: 591px; height: 389px; }
  .envelope .brand-top { top: 22px; gap: 4px; }
  .envelope .brand-top .brand-dot { width: 30px; height: 30px; }
  .envelope .brand-top .brand-name { font-size: 7px; }
  .envelope .brand-main { top: 146px; gap: 8px; }
  .envelope .brand-main .brand-dot { width: 70px; height: 70px; box-shadow: 0 0 0 4px #fff; }
  .envelope .brand-main .brand-name { font-size: 20px; }
  .envelope-address { position: absolute; top: 360px; left: 0; right: 0; text-align: center; font-size: 8px; color: var(--muted); }

  /* Cards */
  .card { width: 245px; height: 143px; }
  .card-front { left: 643px; top: 420px; }
  .card-logo-side { left: 907px; top: 420px; }
  .card-back-green { left: 643px; top: 570px; background: radial-gradient(ellipse at 50% 45%, #8fd14a 0%, var(--green) 35%, var(--dark-green) 90%); }
  .card-back-blue { left: 907px; top: 570px; background: radial-gradient(ellipse at 50% 45%, var(--glow-blue) 0%, var(--deep-blue) 40%, var(--navy) 90%); }

  .card-front .brand { top: 26px; gap: 4px; }
  .card-front .brand-dot { width: 22px; height: 22px; box-shadow: 0 0 0 2px #fff; }
  .card-front .brand-name { font-size: 7.5px; }
  .contact-person { position: absolute; left: 12px; top: 84px; }
  .person-name { font-weight: 600; font-size: 8.5px; }
  .person-title { font-size: 5.5px; color: var(--muted); }
  .contact-details { position: absolute; left: 96px; top: 84px; font-size: 5.5px; line-height: 1.45; color: var(--muted); }

  .card-logo-side .brand { top: 30px; }
  .card-logo-side .brand-dot { width: 46px; height: 46px; }

  .mission { position: absolute; left: 0; right: 0; text-align: center; font-size: 6.5px; font-weight: 600; letter-spacing: .06em; text-transform: uppercase; line-height: 1; }
  .card-logo-side .mission { top: 100px; color: var(--deep-blue); }
  .card-back-green .mission, .card-back-blue .mission { top: 96px; color: #fff; }
  .mission-dot { position: absolute; left: 50%; top: 30px; width: 54px; height: 54px; margin-left: -27px; border-radius: 50%; background: rgba(255,255,255,.85); }
</style>
</head>
<body>

<section class="sheet letterhead">
  <svg class="arc-band" viewBox="0 0 552 66" height="66" preserveAspectRatio="none" aria-hidden="true">
    <defs>
      <radialGradient id="lhGlow" cx="50%" cy="40%" r="55%">
        <stop offset="0" stop-color="#49b6ff"/>
        <stop offset=".45" stop-color="#0b2f8a"/>
        <stop offset="1" stop-color="#0a1230"/>
      </radialGradient>
    </defs>
    <path d="M96 0 H456 Q420 62 276 66 Q132 62 96 0 Z" fill="url(#lhGlow)"/>
  </svg>
  <div class="brand">
    <span class="brand-dot"></span>
    <span class="brand-name">Harbor Logistics</span>
  </div>
  <p class="letterhead-footer">4538 E 61st Pl. Maple Grove, KS 66417-3814 | Phone (913) 555-0148 | www.harborlogisticsco.example</p>
</section>

<section class="sheet envelope">
  <svg class="arc-band" viewBox="0 0 591 190" height="190" preserveAspectRatio="none" aria-hidden="true">
    <defs>
      <radialGradient id="envGlow" cx="50%" cy="45%" r="60%">
        <stop offset="0" stop-color="#49b6ff"/>
        <stop offset=".4" stop-color="#1e7be8"/>
        <stop offset=".75" stop-color="#0b2f8a"/>
        <stop offset="1" stop-color="#0a1230"/>
      </radialGradient>
    </defs>
    <path d="M0 0 H591 V120 Q470 112 420 140 Q360 182 295 184 Q230 182 170 140 Q120 112 0 120 Z" fill="url(#envGlow)"/>
  </svg>
  <div class="brand brand-top">
    <span class="brand-dot"></span>
    <span class="brand-name on-dark">Harbor Logistics</span>
  </div>
  <div class="brand brand-main">
    <span class="brand-dot"></span>
    <span class="brand-name">Harbor Logistics</span>
  </div>
  <p class="envelope-address">4538 E 61st Pl. Maple Grove, KS 66417-3814</p>
</section>

<section class="sheet card card-front">
  <svg class="arc-band" viewBox="0 0 245 36" height="36" preserveAspectRatio="none" aria-hidden="true">
    <defs>
      <radialGradient id="cardGlow" cx="50%" cy="30%" r="60%">
        <stop offset="0" stop-color="#49b6ff"/>
        <stop offset=".5" stop-color="#0b2f8a"/>
        <stop offset="1" stop-color="#0a1230"/>
      </radialGradient>
    </defs>
    <path d="M0 0 H245 V4 Q190 32 122 34 Q55 32 0 4 Z" fill="url(#cardGlow)"/>
  </svg>
  <div class="brand">
    <span class="brand-dot"></span>
    <span class="brand-name">Harbor Logistics</span>
  </div>
  <div class="contact-person">
    <p class="person-name">Calvin Marsh</p>
    <p class="person-title">Director of Operations</p>
  </div>
  <div class="contact-details">
    <p>4538 E 61st Pl. Maple Grove, KS 66417-3814</p>
    <p>Phone (913) 555-0148 &nbsp; Fax (913) 555-0149</p>
    <p>cmarsh@harborlogisticsco.example</p>
    <p>http://www.harborlogisticsco.example</p>
  </div>
</section>

<section class="sheet card card-logo-side">
  <div class="brand">
    <span class="brand-dot"></span>
  </div>
  <p class="mission">Moving Every Day Forward</p>
</section>

<section class="sheet card card-back-green">
  <span class="mission-dot"></span>
  <p class="mission">Moving Every Day Forward</p>
</section>

<section class="sheet card card-back-blue">
  <span class="mission-dot"></span>
  <p class="mission">Moving Every Day Forward</p>
</section>

</body>
</html>
```